CORVEN HIDEWORKS COLLECTIVE BUSINESS CARD
BUSINESS CARD
CORVEN HIDEWORKS COLLECTIVE BUSINESS CARD -
Creative Brief
Use specific fonts
Anything professional
Professional
Hal Durnsey
CEO
512 Wexbury Lane Brellwick, NJ 11284, USA
hdurnsey@corvenhideworks.com
www.corvenhideworks.com
Please add "Alliance of Pelmora Hide Finishers" under our logo.

```html
<!DOCTYPE html>
<html lang="en">
<head>
<meta charset="utf-8">
<title>Corven Hideworks Collective – Business Card</title>
<link href="https://fonts.googleapis.com/css2?family=Crimson+Text:wght@400;600&family=PT+Sans:ital,wght@1,700&display=swap" rel="stylesheet">
<style>
  :root {
    --backdrop: #2a2a2a;
    --card: #ffffff;
    --green: #3f8a1f;
    --green-light: #8cc63f;
    --green-dark: #1f5a12;
    --ink: #2b2b2b;
    --icon: #4a4a4a;
  }
  html, body {
    margin: 0;
    width: 1200px;
    height: 780px;
    overflow: hidden;
    background: var(--backdrop);
  }
  .card {
    position: absolute;
    left: 100px;
    top: 100px;
    width: 1000px;
    height: 580px;
    background: var(--card);
    border-radius: 36px;
    overflow: hidden;
    font-family: "Crimson Text", Georgia, serif;
    color: var(--ink);
  }
  .card__swoosh {
    position: absolute;
    left: 0;
    top: 0;
    width: 1000px;
    height: 580px;
  }
  .brand {
    position: absolute;
    left: 40px;
    top: 170px;
    width: 400px;
    text-align: center;
  }
  .brand__mark {
    width: 64px;
    height: 64px;
    margin: 0 auto 18px;
    background: var(--green);
    border-radius: 50%;
  }
  .brand__name {
    font-weight: 600;
    font-size: 33px;
    line-height: 1.1;
    color: var(--green);
    letter-spacing: 0.5px;
  }
  .brand__tagline {
    margin-top: 10px;
    font-size: 21px;
    color: var(--green-dark);
  }
  .contact {
    position: absolute;
    left: 490px;
    top: 52px;
    width: 480px;
  }
  .contact__name {
    font-family: "PT Sans", Arial, sans-serif;
    font-style: italic;
    font-weight: 700;
    font-size: 34px;
    color: var(--green);
    line-height: 1;
  }
  .contact__role {
    font-family: "PT Sans", Arial, sans-serif;
    font-style: italic;
    font-weight: 700;
    font-size: 20px;
    margin-top: 6px;
  }
  .contact__address {
    margin-top: 26px;
    font-size: 24px;
    line-height: 1.15;
  }
  .contact__list {
    list-style: none;
    margin: 26px 0 0;
    padding: 0;
    font-size: 23px;
    line-height: 1.45;
  }
  .contact__list li {
    display: flex;
    align-items: center;
    gap: 12px;
  }
  .contact__list svg {
    width: 20px;
    height: 20px;
    flex: none;
    fill: var(--icon);
  }
</style>
</head>
<body>
  <div class="card">
    <svg class="card__swoosh" viewBox="0 0 1000 580" aria-hidden="true">
      <defs>
        <linearGradient id="band" x1="0" y1="0" x2="1" y2="0">
          <stop offset="0" stop-color="#1f5a12"/>
          <stop offset="0.5" stop-color="#3f8a1f"/>
          <stop offset="1" stop-color="#8cc63f"/>
        </linearGradient>
      </defs>
      <path d="M0 470 C 250 500, 600 470, 1000 430 L1000 580 L0 580 Z" fill="url(#band)"/>
      <path d="M0 452 C 260 480, 620 455, 1000 410" fill="none" stroke="#111" stroke-width="5"/>
      <path d="M0 478 C 300 505, 640 478, 1000 444" fill="none" stroke="#d8ecc2" stroke-width="3" opacity="0.7"/>
    </svg>

    <div class="brand">
      <div class="brand__mark"></div>
      <div class="brand__name">CORVEN HIDEWORKS<br>COLLECTIVE</div>
      <div class="brand__tagline">Alliance of Pelmora Hide Finishers</div>
    </div>

    <div class="contact">
      <div class="contact__name">Hal Durnsey</div>
      <div class="contact__role">CEO</div>
      <div class="contact__address">512 Wexbury Lane<br>Brellwick, NJ 11284, USA</div>
      <ul class="contact__list">
        <li><svg viewBox="0 0 20 20"><path d="M4 2l4 1 1 4-2 2c1 2 3 4 5 5l2-2 4 1 1 4-2 1C9 18 2 11 2 4z"/></svg>+1 555 014.2000</li>
        <li><svg viewBox="0 0 20 20"><rect x="5" y="1" width="10" height="18" rx="2"/><rect x="7" y="4" width="6" height="9" fill="#fff"/></svg>+1 555 019.8376</li>
        <li><svg viewBox="0 0 20 20"><rect x="5" y="1" width="9" height="6" fill="none" stroke="#4a4a4a" stroke-width="2"/><rect x="2" y="7" width="16" height="9" rx="2"/><rect x="6" y="13" width="8" height="6"/></svg>+1 555 014.2067</li>
        <li><svg viewBox="0 0 20 20"><circle cx="10" cy="10" r="8" fill="none" stroke="#4a4a4a" stroke-width="2"/><circle cx="10" cy="10" r="3.5" fill="none" stroke="#4a4a4a" stroke-width="2"/></svg>hdurnsey@corvenhideworks.com</li>
        <li><svg viewBox="0 0 20 20"><g fill="none" stroke="#4a4a4a" stroke-width="1.6"><circle cx="10" cy="10" r="8"/><ellipse cx="10" cy="10" rx="3.5" ry="8"/><path d="M2 10h16M3.5 6h13M3.5 14h13"/></g></svg>www.corvenhideworks.com</li>
      </ul>
    </div>
  </div>
</body>
</html>
```